Fernvale Craft Works business card design- Fine Art sculpture business (Contract guaranteed)

This business card is for a fine art business. Though we don't have a website up and running yet it should be up soon. I would like the business card to be elegant and fairly simple with a picture of one of my sculptures on the front (you might need to photoshop out the background) as well as my basic contact info (my name,phone # and e-mail). On the back I'd like it to be pretty simple with just "Notes" and some blank lines for writing in info.

Target Market(s)

High end artwork buyers

Industry/Entity Type

Art Gallery

Contact Information for Business Card

Marlo Prewitt Phone: (555) 213-4098 E-mail: marlo@quillbrookmail.com Facebook: @fernvalecraftworks Instagram: fernvalecraftworks

Colors

Designer to choose colors to be used in the design.

Requirements
Must have
• *A picture of one of my sculptures*, my name, business name (Fernvale Craft Works), e-mail, phone #, and a notes section on the back.
• Fernvale Craft Works
• Marlo Prewitt
• (555)213-4098
• marlo@quillbrookmail.com
• Facebook: @fernvalecraftworks
• Instagram: fernvalecraftworks
Nice to have
• It'd be nice if you can crop out the background in the sculpture pictures, which ever one you end up using.

```html
<!DOCTYPE html>
<html lang="en">
<head>
<meta charset="utf-8">
<title>Fernvale Craft Works – Notes Card</title>
<link href="https://fonts.googleapis.com/css2?family=Lato:wght@700&display=swap" rel="stylesheet">
<style>
  :root {
    --page-bg: #ffffff;
    --card-purple: #74449a;
    --card-purple-light: #7b4a9f;
    --card-purple-dark: #6f4296;
    --card-edge: #8e6aae;
    --notes-ink: #b9a0cf;
    --rule-line: rgba(205, 185, 222, 0.55);
  }
  html, body {
    margin: 0;
    padding: 0;
    width: 1200px;
    height: 771px;
    overflow: hidden;
    background: var(--page-bg);
  }
  .canvas {
    position: relative;
    width: 1200px;
    height: 771px;
  }
  .notes-card {
    position: absolute;
    left: 98px;
    top: 59px;
    width: 981px;
    height: 644px;
    box-sizing: border-box;
    border: 1px dashed var(--card-edge);
    overflow: hidden;
  }
  .card-texture {
    position: absolute;
    inset: 0;
    background:
      radial-gradient(ellipse at 55% 20%, var(--card-purple-light) 0%, transparent 55%),
      radial-gradient(ellipse at 20% 80%, var(--card-purple-light) 0%, transparent 50%),
      linear-gradient(135deg, var(--card-purple-dark) 0%, var(--card-purple) 50%, var(--card-purple-dark) 100%);
  }
  .notes-title {
    position: absolute;
    left: 0;
    right: 0;
    top: 158px;
    margin: 0;
    text-align: center;
    font-family: "Lato", sans-serif;
    font-weight: 700;
    font-size: 98px;
    line-height: 1;
    letter-spacing: -1px;
    color: var(--notes-ink);
  }
  .writing-line {
    position: absolute;
    left: 109px;
    width: 763px;
    height: 4px;
    background: var(--rule-line);
  }
  .writing-line--first { top: 267px; }
  .writing-line--second { top: 347px; }
  .writing-line--third { top: 427px; }
</style>
</head>
<body>
  <main class="canvas">
    <section class="notes-card">
      <div class="card-texture" role="img" aria-label="Faint overlapping diamond pattern in shades of purple"></div>
      <h1 class="notes-title">Notes</h1>
      <div class="writing-line writing-line--first"></div>
      <div class="writing-line writing-line--second"></div>
      <div class="writing-line writing-line--third"></div>
    </section>
  </main>
</body>
</html>
```